Packaging box design for start up candle company based in Sydney Australia

I need an eye catching box design for my candle company called Midnight Wickhouse. We specialise only in delicious cake and cocktail scented candles. I want to convey a sense of elegant whimsy.
I have a logo and a style guide which I'm happy with, but need to complete the brand with a stunning box design.
I'd like the same design for two different sized boxes.

```html
<!DOCTYPE html>
<html lang="en">
<head>
<meta charset="utf-8">
<title>Midnight Wickhouse – Candle Box Panels</title>
<link rel="stylesheet" href="https://fonts.googleapis.com/css2?family=Cormorant+Garamond:wght@500&family=Barlow:wght@400;500&display=swap">
<style>
  :root {
    --coral: #e98478;
    --coral-deep: #e07a6e;
    --paper: #ffffff;
    --side: #ececec;
    --ink: #1f1f1f;
    --rule: #9a9a9a;
    --stage: #f4f4f4;
    --serif: "Cormorant Garamond", serif;
    --sans: "Barlow", sans-serif;
  }
  * { box-sizing: border-box; margin: 0; padding: 0; }
  html, body { width: 1200px; height: 675px; overflow: hidden; background: var(--stage); }
  .canvas {
    width: 1200px; height: 675px;
    display: flex; align-items: center; justify-content: center; gap: 40px;
  }
  .panel { position: relative; width: 340px; flex: none; }

  /* Top lid */
  .panel--top {
    height: 340px; background: var(--coral);
    display: flex; align-items: center; justify-content: center;
  }
  .lid-name {
    font-family: var(--serif); font-weight: 500; color: var(--paper);
    font-size: 22px; letter-spacing: 4px; text-align: center; line-height: 1.3;
    text-transform: uppercase;
  }

  /* Front face */
  .panel--front { height: 430px; background: var(--coral); overflow: hidden; }
  .stamp {
    position: absolute; left: 26px; right: 30px; top: 64px; bottom: 0;
    background: var(--paper);
  }
  .stamp-edge { position: absolute; top: 0; bottom: 0; width: 14px; }
  .stamp-edge--left { left: -7px; background: radial-gradient(circle at 7px 8px, var(--paper) 6px, transparent 6.5px) 0 0 / 14px 16px repeat-y; }
  .stamp-edge--right { right: -7px; background: radial-gradient(circle at 7px 8px, var(--paper) 6px, transparent 6.5px) 0 0 / 14px 16px repeat-y; }
  .stamp-edge--top {
    position: absolute; left: 0; right: 0; top: -7px; height: 14px; width: auto;
    background: radial-gradient(circle at 8px 7px, var(--paper) 6px, transparent 6.5px) 0 0 / 16px 14px repeat-x;
  }

  .brand {
    position: absolute; left: 20px; right: 20px; top: 56px;
    display: flex; align-items: center; justify-content: center; gap: 10px;
    padding-bottom: 10px; border-bottom: 1px solid var(--coral);
  }
  .brand-dot { width: 12px; height: 12px; border-radius: 50%; background: var(--coral); flex: none; }
  .brand-name {
    font-family: var(--serif); font-weight: 500; color: var(--ink);
    font-size: 19px; letter-spacing: 3px; text-transform: uppercase; white-space: nowrap;
  }

  .specs {
    position: absolute; left: 0; right: 0; top: 158px; height: 104px;
    border-top: 1px solid var(--rule);
    display: grid; grid-template-columns: 1fr 1fr;
  }
  .specs-size {
    font-family: var(--sans); font-size: 10px; letter-spacing: 0.8px; color: var(--ink);
    padding: 36px 0 0 26px; line-height: 1.9; text-transform: uppercase;
    border-right: 1px solid var(--rule);
  }
  .specs-size small { font-size: 7px; }
  .specs-scent {
    padding: 28px 0 0 12px; font-family: var(--sans); color: var(--ink); text-align: center;
  }
  .scent-type { font-size: 9px; letter-spacing: 1px; text-transform: uppercase; }
  .scent-name { font-size: 21px; font-weight: 500; letter-spacing: 1.5px; line-height: 1.05; margin-top: 6px; text-transform: uppercase; }

  .seal {
    position: absolute; right: 30px; bottom: 30px;
    width: 60px; height: 60px; border-radius: 50%; background: var(--coral-deep);
  }

  /* Side face */
  .panel--side {
    height: 430px; background: var(--side);
    display: flex; align-items: center; justify-content: center; padding: 0 40px;
  }
  .care-copy {
    font-family: var(--sans); color: var(--coral); font-size: 10.5px;
    letter-spacing: 1px; line-height: 1.75; text-transform: uppercase; text-align: left;
  }
</style>
</head>
<body>
  <main class="canvas">
    <section class="panel panel--top" aria-label="Lid">
      <p class="lid-name">Midnight<br>Wickhouse</p>
    </section>

    <section class="panel panel--front" aria-label="Front face">
      <div class="stamp">
        <span class="stamp-edge stamp-edge--left"></span>
        <span class="stamp-edge stamp-edge--right"></span>
        <span class="stamp-edge stamp-edge--top"></span>

        <div class="brand">
          <span class="brand-dot"></span>
          <span class="brand-name">Midnight Wickhouse</span>
        </div>

        <div class="specs">
          <p class="specs-size">7<small>oz</small>&nbsp; Glass<br>36<small>hr</small>&nbsp; Burn</p>
          <div class="specs-scent">
            <p class="scent-type">Scented Wax Candle</p>
            <p class="scent-name">Birthday<br>Cake</p>
          </div>
        </div>

        <span class="seal"></span>
      </div>
    </section>

    <section class="panel panel--side" aria-label="Side face">
      <p class="care-copy">Hand poured in small batches in Sydney, our candles blend soy wax with fine fragrance oils inspired by cakes and cocktails. Trim the wick to five millimetres before each lighting. Burn for no more than three hours at a time. Never leave a burning candle unattended. Keep away from children, pets and anything that can catch fire.</p>
    </section>
  </main>
</body>
</html>
```